BRISK GUARD WEBSITE BANNER DESIGN OF AWESOME

Please take a look at the attached Banner. I want a redesign Idea. The requirements are below.

1)Must Use Website Background
2)Must Use Photo Provided
3)Must Include Button
4)Website the banner will be used on you can see the current at the bottom of the page: https://b.plomvarn.com

Target Market(s)

Anyone Seeking Security Guard Services

```html
<!DOCTYPE html>
<html lang="en">
<head>
<meta charset="utf-8">
<title>Brisk Guard – Get Secured Today</title>
<link rel="stylesheet" href="https://fonts.googleapis.com/css2?family=Poppins:wght@400;500&family=Roboto:wght@500&display=swap">
<style>
  :root {
    --navy-deep: #1b355f;
    --navy: #1e4676;
    --photo-dark: #243f68;
    --photo-mid: #3f6698;
    --photo-light: #8fa9cc;
    --amber: #f9b122;
    --white: #ffffff;
    --button-text: #1f3e6a;
  }
  * { margin: 0; padding: 0; box-sizing: border-box; }
  html, body { width: 1200px; height: 338px; overflow: hidden; background: var(--navy-deep); }
  .banner { position: relative; width: 1200px; height: 338px; overflow: hidden; }
  .banner__backdrop { position: absolute; inset: 0; }
  .banner__photo {
    position: absolute; left: 560px; top: 0; width: 640px; height: 338px;
    background:
      radial-gradient(ellipse 260px 150px at 470px 90px, rgba(200,216,236,0.55), rgba(200,216,236,0) 100%),
      linear-gradient(90deg, rgba(36,63,104,0) 0%, var(--photo-dark) 22%, var(--photo-mid) 70%, var(--photo-mid) 100%);
  }
  .banner__brand-name {
    position: absolute; left: 966px; top: 66px; width: 180px; text-align: center; white-space: nowrap;
    font-family: "Poppins", sans-serif; font-weight: 500; font-size: 16px; letter-spacing: 2px;
    color: rgba(255,255,255,0.28);
  }
  .hero { position: absolute; left: 0; top: 0; width: 818px; height: 338px; text-align: center; }
  .hero__title {
    position: absolute; left: 0; right: 0; top: 80px;
    font-family: "Poppins", sans-serif; font-weight: 500; font-size: 34.5px; line-height: 1;
    color: var(--amber);
  }
  .hero__tagline {
    position: absolute; left: 0; right: 0; top: 131px;
    font-family: "Roboto", sans-serif; font-weight: 500; font-size: 15px; line-height: 1;
    color: var(--white);
  }
  .hero__pointer { position: absolute; left: 402px; top: 167px; }
  .hero__button {
    position: absolute; left: 336px; top: 173px; width: 147px; height: 31px;
    border-radius: 16px; background: var(--amber);
    font-family: "Poppins", sans-serif; font-size: 14px; line-height: 31px;
    color: var(--button-text); text-decoration: none;
  }
  .features {
    position: absolute; left: 232px; top: 233px; display: flex; gap: 12px; list-style: none;
    font-family: "Poppins", sans-serif; font-size: 11px; color: var(--white); white-space: nowrap;
  }
  .features__item { display: flex; align-items: center; gap: 5px; }
</style>
</head>
<body>
<div class="banner">
  <svg class="banner__backdrop" width="1200" height="338" viewBox="0 0 1200 338" aria-hidden="true">
    <rect width="1200" height="338" fill="#1c3e6c"/>
    <polygon points="0,0 620,0 470,338 0,338" fill="#1e4a7c"/>
    <polygon points="0,0 80,68 0,338" fill="#1a5287"/>
    <polygon points="80,68 620,0 400,20" fill="#1d416f"/>
    <polygon points="0,338 160,230 470,338" fill="#1b3963"/>
    <polygon points="620,0 900,0 600,220 470,338" fill="#1b4170"/>
    <polygon points="600,220 470,338 700,338" fill="#1a3660"/>
  </svg>

  <div class="banner__photo" role="img" aria-label="Photo of a security guard shining a flashlight up a stairwell, the beam lighting the company name on the wall"></div>
  <div class="banner__brand-name">BRISK GUARD</div>

  <section class="hero">
    <h1 class="hero__title">Get Secured Today</h1>
    <p class="hero__tagline">WE TAKE YOUR SECURITY PERSONAL.</p>
    <svg class="hero__pointer" width="14" height="9" viewBox="0 0 14 9" aria-hidden="true"><polygon points="0,0 14,0 7,9" fill="#ffffff"/></svg>
    <a class="hero__button" href="https://b.plomvarn.com">Get Started</a>
    <ul class="features">
      <li class="features__item"><svg width="17" height="13" viewBox="0 0 17 13" aria-hidden="true"><path d="M1.5,7 L6,11 L15.5,1.5" fill="none" stroke="#f9b122" stroke-width="3" stroke-linecap="round" stroke-linejoin="round"/></svg>Client Portal</li>
      <li class="features__item"><svg width="17" height="13" viewBox="0 0 17 13" aria-hidden="true"><path d="M1.5,7 L6,11 L15.5,1.5" fill="none" stroke="#f9b122" stroke-width="3" stroke-linecap="round" stroke-linejoin="round"/></svg>24x7 Dispatch</li>
      <li class="features__item"><svg width="17" height="13" viewBox="0 0 17 13" aria-hidden="true"><path d="M1.5,7 L6,11 L15.5,1.5" fill="none" stroke="#f9b122" stroke-width="3" stroke-linecap="round" stroke-linejoin="round"/></svg>No Binding Contracts</li>
    </ul>
  </section>
</div>
</body>
</html>
```